I need a book cover, front and back designed for my e-book Shaping the Craft of Broadcast Pitching. The book provides step-by-step details on how to get you, your products and/or services on radio and television for FREE! The book outlines proven techniques to create effective, targeted messaging the first time and every time!
As an added bonus, I have included "The Twelve Pillars of Persuasion" guaranteed to provide readers the tools and techniques they need to embrace public speaking rather than fearing it.
I envision the back cover to be the reviews that can be found on Vendora http://www.vendora-example.com/SHAPING-CRAFT-BROADCAST-PITCHING-ebook/product-reviews/Z004KTRWX8
My Bio is http://www.halvorkstudios-example.com/bio.html
Updates

We have received several book designs and we are impressed with all of the. Very creative. We are expecting a couple more before the end of this week at e which time we will make our decision with suggested revisions.  Thank you for all your work so far.

 

Tobias

Industry/Entity Type

Radio

Requirements
Must have
• Reviews on back
• Dynamic color(s) preferable dark background with stand out letting
Nice to have
• Because I am in the film and television industry (I am a Director) I think something signifying that such as a film strip my picture in each frame could work out well. I will include a press photo

```html
<!DOCTYPE html>
<html lang="en">
<head>
<meta charset="utf-8">
<title>Shaping the Craft of Broadcast Pitching — Cover</title>
<link rel="stylesheet" href="https://fonts.googleapis.com/css2?family=Oswald:wght@500;600&family=Open+Sans:wght@400&display=swap">
<style>
  :root {
    --page-bg: #e9e9ea;
    --cover-dark: #0c1520;
    --cover-deep: #111c29;
    --title-cyan: #1c9bd8;
    --title-cyan-dim: #1a7fb8;
    --body-text: #0a0f16;
    --panel-navy: #162a44;
    --panel-text: #8fb4d8;
    --art-blue: #1b4a8c;
    --art-violet: #8a3fd6;
  }
  * { margin: 0; padding: 0; box-sizing: border-box; }
  html, body { width: 1200px; height: 800px; overflow: hidden; }
  body {
    background: var(--page-bg);
    font-family: "Open Sans", Arial, sans-serif;
  }
  .cover-spread {
    position: absolute;
    left: 205px;
    top: 110px;
    display: flex;
    height: 580px;
  }
  .back-cover, .front-cover {
    width: 380px;
    height: 580px;
    position: relative;
    overflow: hidden;
  }
  .back-cover {
    background: linear-gradient(180deg, var(--cover-deep) 0%, #1a2a3c 55%, var(--cover-dark) 100%);
    padding: 18px 24px 0;
  }
  .back-author {
    font-family: "Oswald", sans-serif;
    font-weight: 500;
    font-size: 12px;
    color: var(--title-cyan-dim);
    text-align: right;
    padding-right: 50px;
    letter-spacing: 0.5px;
  }
  .title-block {
    font-family: "Oswald", sans-serif;
    font-weight: 600;
    color: var(--title-cyan);
    text-align: center;
    text-transform: uppercase;
    line-height: 1;
  }
  .back-cover .title-block { color: var(--title-cyan-dim); }
  .title-main { display: block; }
  .title-mid {
    display: flex;
    align-items: center;
    justify-content: center;
    gap: 12px;
  }
  .title-bar {
    display: inline-block;
    height: 0.22em;
    width: 1.3em;
    background: currentColor;
  }
  .back-cover .title-main { font-size: 50px; }
  .back-cover .title-mid { font-size: 30px; margin: 4px 0; }
  .back-cover .title-last { font-size: 30px; display: block; }
  .back-blurb {
    margin-top: 14px;
    font-size: 10.4px;
    line-height: 1.32;
    color: var(--body-text);
    text-align: justify;
    text-align-last: center;
  }
  .back-panels {
    position: absolute;
    left: 22px;
    right: 22px;
    bottom: 24px;
    display: flex;
    justify-content: space-between;
  }
  .back-panel {
    width: 100px;
    height: 46px;
    background: var(--panel-navy);
    color: var(--panel-text);
    font-size: 10px;
    display: flex;
    align-items: center;
    justify-content: center;
  }
  .spine {
    width: 30px;
    height: 580px;
    background: var(--cover-dark);
    display: flex;
    align-items: center;
    justify-content: flex-start;
    writing-mode: vertical-rl;
    padding-top: 10px;
    gap: 20px;
  }
  .spine-title {
    font-family: "Oswald", sans-serif;
    font-weight: 600;
    font-size: 17px;
    color: var(--title-cyan);
    text-transform: uppercase;
    letter-spacing: 0.5px;
  }
  .spine-author {
    font-family: "Oswald", sans-serif;
    font-size: 8px;
    color: var(--panel-text);
    text-transform: uppercase;
  }
  .front-cover { background: var(--cover-dark); }
  .front-cover .title-block { padding-top: 16px; }
  .front-cover .title-main { font-size: 78px; }
  .front-cover .title-mid { font-size: 42px; margin: 2px 0; }
  .front-cover .title-last { font-size: 42px; display: block; }
  .front-art {
    position: absolute;
    left: 0;
    right: 0;
    top: 210px;
    height: 330px;
    background:
      radial-gradient(ellipse at 50% 55%, rgba(170, 90, 230, 0.85) 0%, rgba(60, 90, 200, 0.55) 25%, rgba(20, 50, 110, 0.3) 55%, transparent 80%),
      linear-gradient(180deg, var(--cover-dark) 0%, var(--art-blue) 45%, #0e1a2c 100%);
  }
  .front-author-band {
    position: absolute;
    left: 0;
    right: 0;
    bottom: 0;
    height: 40px;
    background: var(--cover-dark);
    display: flex;
    align-items: center;
    justify-content: center;
    font-family: "Oswald", sans-serif;
    font-weight: 500;
    font-size: 15px;
    color: var(--title-cyan);
    text-transform: uppercase;
    letter-spacing: 0.5px;
  }
</style>
</head>
<body>
  <main class="cover-spread">
    <section class="back-cover">
      <p class="back-author">TOBIAS S. HALVORK</p>
      <h2 class="title-block">
        <span class="title-main">Shaping</span>
        <span class="title-mid"><span class="title-bar"></span>The Craft of<span class="title-bar"></span></span>
        <span class="title-last">Broadcast Pitching</span>
      </h2>
      <p class="back-blurb">Lorem ipsum dolor sit amet, consectetur adipisicing elit, sed do eiusmod tempor incididunt ut labore et dolore magna aliqua. Ut enim ad minim veniam, quis nostrud exercitation. Lorem ipsum dolor sit amet, consectetur adipisicing elit, sed do eiusmod tempor incididunt ut labore et dolore magna aliqua. Ut enim ad minim veniam, quis nostrud exercitation. Lorem ipsum dolor sit amet, consectetur adipisicing elit, sed do eiusmod tempor incididunt ut labore et dolore magna aliqua. Ut enim ad minim veniam, quis nostrud exercitation. Lorem ipsum dolor sit amet, consectetur adipisicing elit, sed do eiusmod tempor incididunt ut labore et dolore magna aliqua. Ut enim ad minim veniam, quis nostrud exercitation. Lorem ipsum dolor sit amet, consectetur adipisicing elit, sed do eiusmod tempor incididunt ut labore et dolore magna aliqua. Ut enim ad minim veniam, quis nostrud exercitation. Lorem ipsum dolor sit amet, consectetur adipisicing elit, sed do eiusmod tempor incididunt ut labore et dolore magna aliqua. Ut enim ad minim veniam, quis nostrud exercitation. Lorem ipsum dolor sit amet, consectetur adipisicing elit, sed do eiusmod tempor incididunt ut labore et dolore magna aliqua. Ut enim ad minim veniam, quis nostrud exercitation. Lorem ipsum dolor sit amet, consectetur adipisicing elit, sed do eiusmod tempor incididunt ut labore et dolore magna aliqua. Ut enim ad minim veniam, quis nostrud exercitation. Lorem ipsum dolor sit amet, consectetur adipisicing elit, sed do eiusmod tempor incididunt ut labore et dolore magna aliqua. Ut enim ad minim veniam, quis nostrud exercitation.</p>
      <div class="back-panels">
        <div class="back-panel">LOGO</div>
        <div class="back-panel">ISBN</div>
      </div>
    </section>

    <div class="spine">
      <span class="spine-title">Shaping the Craft of Broadcast Pitching</span>
      <span class="spine-author">Tobias S. Halvork</span>
    </div>

    <section class="front-cover">
      <h1 class="title-block">
        <span class="title-main">Shaping</span>
        <span class="title-mid"><span class="title-bar"></span>The Craft of<span class="title-bar"></span></span>
        <span class="title-last">Broadcast Pitching</span>
      </h1>
      <div class="front-art" role="img" aria-label="Photo of a businessman's open hand holding glowing media icons: a laptop, envelopes, a globe and a tablet over a world map"></div>
      <p class="front-author-band">Tobias S. Halvork</p>
    </section>
  </main>
</body>
</html>
```